K.T.L Electrical Services Pty Ltd

Electrical contracting business. I have a base for the design which i like. The contact number needs to be changed to 0491736250 and the O made more solid and level with the rest of the letters. If you have any other ideas of what would make it better I'm happy to see them.

The back side to be written as dot points with the following:
- Residential & Commercial
- Maintenance
- PV & Battery servicing
- EV Chargers

```html
<!DOCTYPE html>
<html lang="en">
<head>
<meta charset="utf-8">
<title>K.T.L Electrical Services – Business Card</title>
<link rel="stylesheet" href="https://fonts.googleapis.com/css2?family=Montserrat:wght@300;400;500;600;700&display=swap">
<style>
  :root {
    --backdrop: #999999;
    --card: #1e292e;
    --card-deep: #151819;
    --ring: #1f2c31;
    --teal: #8fadad;
    --white: #ffffff;
  }
  * { margin: 0; padding: 0; box-sizing: border-box; }
  html, body {
    width: 1200px; height: 1000px; overflow: hidden;
    background: var(--backdrop);
    font-family: "Montserrat", sans-serif;
  }
  .canvas { position: relative; width: 1200px; height: 1000px; }
  .card {
    position: absolute; left: 276px; width: 650px; height: 374px;
    background: var(--card); border-radius: 26px; overflow: hidden;
  }
  .card--front { top: 103px; }
  .card--back { top: 522px; }

  /* Front */
  .front-wordmark {
    position: absolute; left: 0; right: 0; top: 62px;
    text-align: center; color: var(--teal);
    font-weight: 500; font-size: 150px; line-height: 1; letter-spacing: 2px;
  }
  .front-tagline {
    position: absolute; left: 0; right: 0; top: 215px;
    text-align: center; color: var(--teal);
    font-weight: 500; font-size: 31px; letter-spacing: 1px; line-height: 1;
  }
  .services {
    position: absolute; left: 30px; right: 30px; top: 285px;
    list-style: none; text-align: center; color: var(--white);
    font-size: 16px; font-weight: 500; line-height: 28px;
  }
  .services li { display: inline; }
  .services li + li::before {
    content: "•"; color: var(--teal); margin: 0 7px 0 6px;
  }
  .services li.wrap::before { margin-left: 0; }
  .services li.wrap { display: block; }

  /* Back */
  .rings { position: absolute; inset: 0; }
  .contact {
    position: absolute; left: 30px; top: 278px; width: 232px;
    transform-origin: top left; transform: rotate(-90deg);
    text-align: right; color: var(--white); font-weight: 300;
  }
  .contact__name {
    color: var(--teal); font-weight: 700; font-size: 29px; line-height: 32px;
    letter-spacing: 0.5px;
  }
  .contact__role { font-size: 19px; line-height: 24px; margin-bottom: 20px; }
  .contact__line { font-size: 21px; line-height: 28px; }

  .back-brand {
    position: absolute; right: 27px; top: 195px; text-align: right;
    color: var(--teal); font-weight: 500; line-height: 1;
  }
  .back-brand__mark { font-size: 106px; letter-spacing: 1px; }
  .back-brand__tagline { font-size: 22px; letter-spacing: 0.6px; margin-top: 6px; }
  .back-brand__licence { font-size: 19px; letter-spacing: 0.5px; margin-top: 7px; }
</style>
</head>
<body>
<main class="canvas">
  <section class="card card--front" aria-label="Card front">
    <div class="front-wordmark">K.T.L</div>
    <div class="front-tagline">ELECTRICAL SERVICES P/L</div>
    <ul class="services">
      <li>Residential &amp; Commercial</li>
      <li>Maintenance</li>
      <li>PV &amp; Battery servicing</li>
      <li class="wrap">EV Chargers</li>
    </ul>
  </section>

  <section class="card card--back" aria-label="Card back">
    <svg class="rings" width="650" height="374" viewBox="0 0 650 374" aria-hidden="true">
      <circle cx="494" cy="303" r="283" fill="var(--card-deep)"/>
      <circle cx="494" cy="303" r="271" fill="var(--ring)"/>
      <circle cx="494" cy="303" r="258" fill="var(--card-deep)"/>
      <circle cx="494" cy="303" r="246" fill="var(--ring)"/>
      <circle cx="494" cy="303" r="233" fill="#141515"/>
    </svg>
    <div class="contact">
      <div class="contact__name">DANIEL FORDE</div>
      <div class="contact__role">Owner</div>
      <div class="contact__line">0491 736 250</div>
      <div class="contact__line">info@ktlelectrical.com</div>
    </div>
    <div class="back-brand">
      <div class="back-brand__mark">K.T.L</div>
      <div class="back-brand__tagline">ELECTRICAL SERVICES P/L</div>
      <div class="back-brand__licence">EC 20418</div>
    </div>
  </section>
</main>
</body>
</html>
```